Looking for a tri-fold flyer for a new energy conservation company

We are a locally owned energy conservation company that focuses on making energy efficiency upgrades to residential, commercial, and agricultural properties. Services range from solar, re-roofs, dual pane windows, HVAC's, tankless water heaters, water efficient products, I have a list of items I can upload to show all services and pictures of a website that we are building currently. I would like the tri fold to include who, what, why info I have attached. I would like to see a modern design with Bold Capitalized text, our blue color to be used a lot with the green maybe accent colors.

Target Market(s)

please see attachment

Industry/Entity Type

It Company

Requirements
Must have
• please see attachment
Nice to have
• please see attachment
Should not have
• Colors requested below are in the logo that is attached as a PSD file.

```html
<!DOCTYPE html>
<html lang="en">
<head>
<meta charset="utf-8">
<title>Brightleaf Contractors – Tri-fold Brochure</title>
<link href="https://fonts.googleapis.com/css2?family=Boogaloo&family=Roboto+Slab:wght@500;600&display=swap" rel="stylesheet">
<style>
  :root{
    --page:#e6e7ea;
    --blue:#1a9fdc;
    --blue-light:#3cc3f2;
    --blue-deep:#0d7cc0;
    --green:#a2d12c;
    --green-deep:#6ea51b;
    --white:#ffffff;
    --fold:rgba(255,255,255,.18);
  }
  *{box-sizing:border-box;margin:0;padding:0}
  html,body{width:1200px;height:1046px;overflow:hidden;background:var(--page)}
  body{position:relative;font-family:"Roboto Slab",serif;color:var(--white)}
  .sheet{position:absolute;left:40px;width:1120px;height:460px;overflow:hidden;box-shadow:0 6px 18px rgba(0,0,0,.18)}
  .sheet--inside{top:40px}
  .sheet--outside{top:546px}
  .sheet__art{position:absolute;inset:0;width:1120px;height:460px}
  .service-line{font-family:"Boogaloo",sans-serif;font-size:17px;fill:var(--white);letter-spacing:.5px}
  .panel{position:absolute;top:0;width:373px;height:460px;text-align:center}
  .panel--1{left:0}.panel--2{left:373px}.panel--3{left:747px}
  .icon-ring{position:absolute;left:50%;width:70px;height:70px;margin-left:-35px;border-radius:50%;border:4px solid var(--green);background:var(--blue-deep)}
  .panel__title{position:absolute;left:0;right:0;font-family:"Boogaloo",sans-serif;font-weight:400;font-size:36px;letter-spacing:.5px;text-transform:uppercase}
  .panel__body{position:absolute;left:36px;right:36px;font-size:12.5px;line-height:1.36;font-weight:500;text-align:left}
  .panel__body strong{font-weight:600;letter-spacing:.4px}
  .placeholder{position:absolute}
  .globe{left:131px;top:55px;width:110px;height:110px;border-radius:50%;background:radial-gradient(circle at 35% 35%,#ffffff,#cfe3a8 60%,#8fbf3a)}
  .pill{position:absolute;left:76px;top:180px;width:220px;height:40px;border-radius:20px;background:var(--green);font-family:"Boogaloo",sans-serif;font-size:30px;line-height:40px;text-transform:uppercase}
  .bulb{left:80px;top:36px;width:212px;height:220px;border-radius:90px 90px 30px 30px;background:radial-gradient(circle at 50% 40%,#f4fbff,#bfe6d4 55%,#7fb07a)}
  .contact{position:absolute;left:20px;right:20px;top:300px;font-family:"Boogaloo",sans-serif;font-size:18px;line-height:1.3;letter-spacing:.6px;text-transform:uppercase}
  .tree{left:96px;top:34px;width:180px;height:200px;border-radius:50% 50% 12px 12px;background:linear-gradient(#b6dd4a,#8cbf2c 70%,#8a8f95)}
  .brand{position:absolute;left:0;right:0;top:270px;display:flex;align-items:center;justify-content:center;gap:10px}
  .brand__dot{width:22px;height:22px;border-radius:50%;background:var(--green)}
  .brand__name{font-size:28px;font-weight:600;color:var(--green)}
</style>
</head>
<body>

<section class="sheet sheet--inside" aria-label="Brochure inside">
  <svg class="sheet__art" viewBox="0 0 1120 460" aria-hidden="true">
    <defs>
      <radialGradient id="inBlue" cx="50%" cy="50%" r="65%">
        <stop offset="0" stop-color="#49c9f4"/>
        <stop offset="1" stop-color="#1592d4"/>
      </radialGradient>
      <path id="topArc" d="M0 110 Q560 -40 1120 110"/>
      <path id="bottomArc" d="M0 385 Q560 505 1120 385"/>
    </defs>
    <rect width="1120" height="460" fill="url(#inBlue)"/>
    <path d="M0 135 Q560 -15 1120 135 L1120 168 Q560 18 0 168Z" fill="var(--green)"/>
    <path d="M0 160 Q560 10 1120 160 L1120 168 Q560 18 0 168Z" fill="var(--green-deep)" opacity=".5"/>
    <path d="M0 320 Q560 440 1120 320 L1120 352 Q560 472 0 352Z" fill="var(--green)"/>
    <path d="M0 320 Q560 440 1120 320 L1120 328 Q560 448 0 328Z" fill="var(--green-deep)" opacity=".5"/>
    <text class="service-line"><textPath href="#topArc" startOffset="50%" text-anchor="middle">SOLOR PANELS  •  LIGHTING  •  HEATING &amp; A/C  •  ROOFING  •  WINDOWS &amp; DOORS  •  INSULATION</textPath></text>
    <text class="service-line"><textPath href="#bottomArc" startOffset="50%" text-anchor="middle">RESIDENTIAL  •  COMMERCIAL  •  AGRICULTURAL  •  PUBLIC SECTOR</textPath></text>
    <line x1="373" y1="0" x2="373" y2="460" stroke="var(--fold)" stroke-width="2"/>
    <line x1="747" y1="0" x2="747" y2="460" stroke="var(--fold)" stroke-width="2"/>
  </svg>

  <article class="panel panel--1">
    <div class="icon-ring" style="top:85px" role="img" aria-label="Leaf icon"></div>
    <h2 class="panel__title" style="top:175px">Who We Are</h2>
    <p class="panel__body" style="top:222px"><strong>Brightleaf Contractors</strong> is your all-in-one energy conservation improvement contractor. We help homeowners, business owners, and the private sector reduce energy costs while reducing their carbon footprint.</p>
  </article>

  <article class="panel panel--2">
    <div class="icon-ring" style="top:42px" role="img" aria-label="Hand holding a seedling icon"></div>
    <h2 class="panel__title" style="top:130px">With Our Help</h2>
    <p class="panel__body" style="top:178px"><strong>Brightleaf Contractors</strong> will provide our customers comfort all year round by reducing energy usage and utility bills; saving you money. Making such improvements increases the value of your home and adds even greater curb appeal. We provide multiple financing options and discuss each of these with our customers to provide the best service possible. We also provide 100% financing meaning no money out of pocket from you.</p>
  </article>

  <article class="panel panel--3">
    <div class="icon-ring" style="top:85px" role="img" aria-label="House icon"></div>
    <h2 class="panel__title" style="top:175px">What We Offer</h2>
    <p class="panel__body" style="top:222px"><strong>Brightleaf Contractors</strong> offers the best available energy efficient products on the market with competitive pricing. Our multiple licenses and insurance policies allow us to provide competitive pricing options to our customers by packaging several energy efficient products together.</p>
  </article>
</section>

<section class="sheet sheet--outside" aria-label="Brochure outside">
  <svg class="sheet__art" viewBox="0 0 1120 460" aria-hidden="true">
    <defs>
      <linearGradient id="outBlue" x1="0" y1="0" x2="1" y2="1">
        <stop offset="0" stop-color="#2bb2e8"/>
        <stop offset=".6" stop-color="#1aa0dd"/>
        <stop offset="1" stop-color="#38c1f1"/>
      </linearGradient>
    </defs>
    <rect width="1120" height="460" fill="url(#outBlue)"/>
    <path d="M0 0 H1120 V20 Q400 10 0 95Z" fill="var(--blue-light)"/>
    <path d="M0 95 Q400 10 1120 20 L1120 55 Q400 40 0 130Z" fill="var(--green)"/>
    <path d="M0 122 Q400 32 1120 48 L1120 55 Q400 40 0 130Z" fill="var(--green-deep)" opacity=".5"/>
    <path d="M0 400 Q600 330 1120 380 L1120 412 Q600 362 0 432Z" fill="var(--green)"/>
    <path d="M0 432 Q600 362 1120 412 L1120 460 H0Z" fill="var(--blue-deep)"/>
    <line x1="373" y1="0" x2="373" y2="460" stroke="var(--fold)" stroke-width="2"/>
    <line x1="747" y1="0" x2="747" y2="460" stroke="var(--fold)" stroke-width="2"/>
  </svg>

  <article class="panel panel--1">
    <div class="placeholder globe" role="img" aria-label="Globe illustration"></div>
    <h2 class="pill">About Us</h2>
    <p class="panel__body" style="top:232px;font-size:12.8px"><strong>Brightleaf Contractors</strong> is a local company in Lakeport, CA with over 25 years of experience in all aspects of construction. We are the only business that specializes in total home and business energy conservation. We offer detailed financial analysis of all considered improvements to ensure you make the best decision possible. We pride ourselves in providing exceptional service, quality products, and competitive pricing. These core values set us apart from other providers in our industry, and we look forward to working with you.</p>
  </article>

  <article class="panel panel--2">
    <div class="placeholder bulb" role="img" aria-label="Light bulb with green plant growing inside"></div>
    <address class="contact" style="font-style:normal">
      4100 Harbor View Rd, Ste 12<br>
      Lakeport, CA 90000<br>
      Ph: 555.201.0411 • Fax: 555.201.0882<br>
      brightleafcontractors.com
    </address>
  </article>

  <article class="panel panel--3">
    <div class="placeholder tree" role="img" aria-label="Tree with green leaves illustration"></div>
    <div class="brand">
      <span class="brand__dot"></span>
      <span class="brand__name">Brightleaf Contractors</span>
    </div>
  </article>
</section>

</body>
</html>
```